Medical Practice Business Card

we need a business card for our new medical ophthalmology practice based in Needham Massachusetts. we are looking for a simple , modern and elegant design.
the card needs to contain the following
1- the logo of our practice (please see attached file)
2- the name of the practice : "Silver Birch Retina Care"
3- Doctor's Name: Tobias Rendell MD PhD
4- Specialty: Board-Certified Vitreoretinal Surgeon
5- practice address: 87 Larkspur Ave, Suite 210, Needham MA 02481
7- Office number: 617- 482 - 7730
8- fax number: 617- 391 - 2268
9- email: info@sbretinahub.example
10- website: www.sbretinahub.example

```html
<!DOCTYPE html>
<html lang="en">
<head>
<meta charset="utf-8">
<title>Silver Birch Retina Care – Business Card</title>
<link href="https://fonts.googleapis.com/css2?family=Open+Sans:wght@400;600;700&display=swap" rel="stylesheet">
<style>
  :root{
    --bg:#e9e7e4;
    --card-white:#fbfbfb;
    --card-black:#151515;
    --navy:#1f4d7a;
    --sky:#3c8ccb;
    --grey:#5f6366;
    --rule:#2c5885;
    --back-ink:#4a4a4a;
  }
  *{margin:0;padding:0;box-sizing:border-box}
  html,body{width:1200px;height:900px;overflow:hidden}
  body{background:var(--bg);font-family:"Open Sans",Arial,sans-serif;position:relative}
  .card{position:absolute;left:250px;width:700px;height:400px;box-shadow:0 6px 18px rgba(0,0,0,.18)}
  .card--front{top:33px;background:var(--card-white)}
  .card--back{top:467px;background:linear-gradient(135deg,#262626,var(--card-black))}

  .brand{position:absolute;left:60px;top:160px;display:flex;align-items:center;gap:14px}
  .brand__dot{width:16px;height:16px;border-radius:50%;background:var(--navy);flex:none}
  .brand__name{font-size:24px;font-weight:600;color:var(--navy);letter-spacing:.5px;line-height:1.2;width:230px}

  .divider{position:absolute;left:355px;top:90px;width:2px;height:220px;background:var(--rule)}

  .details{position:absolute;left:385px;top:92px;width:300px}
  .details__name{font-size:24px;font-weight:700;color:var(--navy);line-height:1.1}
  .details__role{font-size:13.5px;color:var(--sky);margin-top:3px}
  .details__address{font-size:14px;color:var(--grey);margin-top:16px;line-height:1.35}
  .contact{list-style:none;margin-top:8px}
  .contact li{display:flex;align-items:center;gap:12px;font-size:14px;color:var(--grey);line-height:1.75}
  .contact svg{width:15px;height:15px;flex:none}

  .back-brand{position:absolute;inset:0;display:flex;align-items:center;justify-content:center;gap:20px}
  .back-brand__dot{width:40px;height:40px;border-radius:50%;background:var(--back-ink)}
  .back-brand__name{font-size:40px;font-weight:600;color:var(--back-ink);letter-spacing:1px;line-height:1.15;width:330px}
</style>
</head>
<body>
  <section class="card card--front">
    <div class="brand">
      <span class="brand__dot"></span>
      <span class="brand__name">Silver Birch Retina Care</span>
    </div>
    <div class="divider"></div>
    <div class="details">
      <h1 class="details__name">Tobias Rendell MD PhD</h1>
      <p class="details__role">Board-Certified Vitreoretinal Surgeon</p>
      <p class="details__address">87 Larkspur Ave, Suite<br>210, Needham MA 02481</p>
      <ul class="contact">
        <li><svg viewBox="0 0 16 16" aria-hidden="true"><path fill="#2f4a63" d="M2 6c0-2 3-3 6-3s6 1 6 3l-2 1-1-2H5L4 7zM4 8h8l1 5H3z"/><circle cx="8" cy="10.5" r="1.5" fill="#fff"/></svg>617- 482 - 7730</li>
        <li><svg viewBox="0 0 16 16" aria-hidden="true"><circle cx="8" cy="8" r="7.5" fill="#2f4a63"/><rect x="4" y="6" width="8" height="5" rx="1" fill="#fff"/><rect x="5.5" y="4" width="5" height="2.5" fill="#fff"/></svg>617- 391 - 2268</li>
        <li><svg viewBox="0 0 16 16" aria-hidden="true"><rect x="1" y="3" width="14" height="10" fill="none" stroke="#2f4a63" stroke-width="1.6"/><path d="M1 3l7 6 7-6" fill="none" stroke="#2f4a63" stroke-width="1.6"/></svg>info@sbretinahub.example</li>
        <li><svg viewBox="0 0 16 16" aria-hidden="true"><g fill="none" stroke="#2f4a63" stroke-width="1.3"><circle cx="8" cy="8" r="6.5"/><ellipse cx="8" cy="8" rx="3" ry="6.5"/><path d="M1.5 8h13M3 4.5h10M3 11.5h10"/></g></svg>www.sbretinahub.example</li>
      </ul>
    </div>
  </section>

  <section class="card card--back">
    <div class="back-brand">
      <span class="back-brand__dot"></span>
      <span class="back-brand__name">Silver Birch Retina Care</span>
    </div>
  </section>
</body>
</html>
```